Covid 19 Exit Strategy one page brochure

I would like to design, and will need URGENT help, a brochure detailing a Covid 19 Exit Strategy plan. This brochure will need to be understood easily and the graphics inside should make it easy for people to understand without reading the entire text. This project is quite urgent and needs to be completed THIS WEEK - by Saturday may 16th at the latest. I am attaching two examples. I will provide the text.

```html
<!DOCTYPE html>
<html lang="en">
<head>
<meta charset="utf-8">
<title>Coronavirus COVID-19 – The Exit Strategy</title>
<link rel="stylesheet" href="https://fonts.googleapis.com/css2?family=Montserrat:wght@400;500;700;800;900&display=swap">
<style>
  :root {
    --navy: #173b5c;
    --ink: #1d1d1f;
    --white: #ffffff;
    --red: #e61f52;
    --orange: #f7a12a;
    --yellow: #f9d447;
    --flame: #ee4a23;
    --amber: #f59a22;
    --magenta: #b52a8f;
    --pink: #e45fa7;
    --teal: #139a8c;
    --aqua: #54c6b6;
    --lime: #d5e02a;
    --green: #6abf45;
    --track: #cfd9de;
    --dash: #c9cbcd;
    --map: #45506a;
  }
  * { margin: 0; padding: 0; box-sizing: border-box; }
  html, body { width: 900px; height: 1200px; overflow: hidden; background: var(--white); }
  .brochure {
    position: relative; width: 900px; height: 1200px; overflow: hidden;
    font-family: "Montserrat", sans-serif; background: var(--white);
  }
  .artwork { position: absolute; inset: 0; }
  .header-title {
    position: absolute; left: 173px; top: 112px; color: var(--white);
    font-weight: 800; font-size: 34px; line-height: 1; letter-spacing: -0.3px;
  }
  .header-subtitle {
    position: absolute; left: 174px; top: 162px; color: var(--white);
    font-weight: 500; font-size: 24px; line-height: 1; letter-spacing: 0.2px;
  }
  .hub-label {
    position: absolute; left: 110px; width: 220px; text-align: center;
    color: var(--navy); font-weight: 900; line-height: 1;
  }
  .hub-label--the { top: 508px; font-size: 25px; }
  .hub-label--exit { top: 538px; font-size: 68px; letter-spacing: -3px; }
  .hub-label--strategy { top: 603px; font-size: 29px; letter-spacing: -0.5px; }
  .step-text {
    position: absolute; color: var(--white); font-size: 11.4px; line-height: 15.5px;
    text-align: justify; letter-spacing: 0.1px;
  }
  .step-text strong { display: block; font-size: 18px; font-weight: 700; line-height: 22px; text-align: left; }
  .step-text--hospital { left: 475px; top: 300px; width: 150px; font-size: 12.5px; text-align: left; line-height: 17px; }
  .step-text--resurgence { left: 525px; top: 433px; width: 178px; }
  .step-text--monitoring { left: 583px; top: 572px; width: 178px; }
  .step-text--testing { left: 523px; top: 711px; width: 178px; }
  .step-text--barriers { left: 461px; top: 834px; width: 180px; }
  .closing {
    position: absolute; left: 172px; top: 960px; color: var(--ink);
    font-size: 38px; line-height: 47px; font-weight: 400; letter-spacing: -0.5px;
  }
  .closing b { color: var(--navy); font-weight: 800; }
</style>
</head>
<body>
<main class="brochure">
  <svg class="artwork" width="900" height="1200" viewBox="0 0 900 1200" aria-hidden="false">
    <defs>
      <linearGradient id="grad-header" x1="0" x2="1"><stop offset="0" stop-color="var(--orange)"/><stop offset="1" stop-color="var(--yellow)"/></linearGradient>
      <linearGradient id="grad-hospital" x1="0" x2="1"><stop offset="0" stop-color="var(--orange)"/><stop offset="1" stop-color="var(--yellow)"/></linearGradient>
      <linearGradient id="grad-resurgence" x1="0" x2="1"><stop offset="0" stop-color="var(--flame)"/><stop offset="1" stop-color="var(--amber)"/></linearGradient>
      <linearGradient id="grad-monitoring" x1="0" x2="1"><stop offset="0" stop-color="var(--magenta)"/><stop offset="1" stop-color="var(--pink)"/></linearGradient>
      <linearGradient id="grad-testing" x1="0" x2="1"><stop offset="0" stop-color="var(--teal)"/><stop offset="1" stop-color="var(--aqua)"/></linearGradient>
      <linearGradient id="grad-barriers" x1="0" x2="1"><stop offset="0" stop-color="var(--lime)"/><stop offset="1" stop-color="var(--green)"/></linearGradient>
      <linearGradient id="grad-hub" x1="0" y1="0" x2="1" y2="1"><stop offset="0" stop-color="#ffffff"/><stop offset="1" stop-color="#dcdde0"/></linearGradient>
      <filter id="soft-shadow" x="-20%" y="-20%" width="140%" height="150%"><feDropShadow dx="0" dy="5" stdDeviation="5" flood-color="#000" flood-opacity="0.22"/></filter>
      <g id="step-shape">
        <polygon points="0,56 56,0 294,0 350,56 294,112 56,112"/>
      </g>
    </defs>

    <!-- header band -->
    <polygon class="header-accent" points="0,68 112,80 118,226 0,240" fill="var(--red)"/>
    <polygon class="header-band" points="112,92 900,65 900,226 118,212" fill="url(#grad-header)"/>

    <!-- orbit guides -->
    <path class="orbit-dash" d="M220,402 A199,199 0 0 1 220,800" fill="none" stroke="var(--dash)" stroke-width="2" stroke-dasharray="4 4"/>
    <path class="orbit-track" d="M220,445 A156,156 0 0 1 220,757" fill="none" stroke="var(--track)" stroke-width="10"/>

    <!-- connectors -->
    <g class="connectors" fill="none" stroke="#8ea1ab" stroke-width="1.2">
      <polyline points="287,428 307,365 353,365"/>
      <polyline points="363,484 373,462 390,462"/>
      <polyline points="402,601 446,601"/>
      <polyline points="364,719 373,741 390,741"/>
      <polyline points="289,775 309,837 355,837"/>
    </g>
    <g class="connector-ends" fill="#8ea1ab">
      <circle cx="287" cy="428" r="3"/><circle cx="353" cy="365" r="2.5"/>
      <circle cx="363" cy="484" r="3"/><circle cx="390" cy="462" r="2.5"/>
      <circle cx="402" cy="601" r="3"/><circle cx="446" cy="601" r="2.5"/>
      <circle cx="364" cy="719" r="3"/><circle cx="390" cy="741" r="2.5"/>
      <circle cx="289" cy="775" r="3"/><circle cx="355" cy="837" r="2.5"/>
    </g>
    <g class="orbit-dots" stroke="#fff" stroke-width="4" filter="url(#soft-shadow)">
      <circle cx="281" cy="450" r="10" fill="var(--orange)"/>
      <circle cx="343" cy="500" r="10" fill="var(--flame)"/>
      <circle cx="375" cy="601" r="10" fill="var(--magenta)"/>
      <circle cx="343" cy="700" r="10" fill="var(--teal)"/>
      <circle cx="281" cy="751" r="10" fill="var(--green)"/>
    </g>

    <!-- central hub -->
    <circle class="hub-ring" cx="220" cy="600" r="122" fill="#e9eaec" filter="url(#soft-shadow)"/>
    <circle class="hub-disc" cx="220" cy="600" r="110" fill="url(#grad-hub)"/>
    <rect class="hub-map" x="182" y="640" width="87" height="54" rx="6" fill="var(--map)" role="img" aria-label="World map silhouette"/>

    <!-- steps -->
    <g class="step step--hospital" transform="translate(336,273)" filter="url(#soft-shadow)">
      <use href="#step-shape" fill="url(#grad-hospital)"/>
      <polygon points="0,56 56,0 112,56 56,112" fill="url(#grad-hospital)"/>
      <g fill="none" stroke="#fff" stroke-width="2.5">
        <rect x="42" y="32" width="28" height="42"/><rect x="22" y="44" width="20" height="30"/><rect x="70" y="44" width="20" height="30"/>
        <line x1="56" y1="36" x2="56" y2="48"/><line x1="50" y1="42" x2="62" y2="42"/><rect x="51" y="62" width="10" height="12"/>
        <line x1="18" y1="76" x2="94" y2="76"/>
      </g>
    </g>
    <g class="step step--resurgence" transform="translate(399,406)" filter="url(#soft-shadow)">
      <use href="#step-shape" fill="url(#grad-resurgence)"/>
      <polygon points="0,56 56,0 112,56 56,112" fill="url(#grad-resurgence)"/>
      <g fill="none" stroke="#fff" stroke-width="2.2">
        <polyline points="36,58 58,38 80,58"/><polyline points="42,53 42,80 76,80 76,53"/><rect x="54" y="64" width="10" height="16"/>
        <circle cx="44" cy="34" r="7"/><line x1="44" y1="30" x2="44" y2="35"/>
        <line x1="22" y1="70" x2="34" y2="70"/><polyline points="30,66 34,70 30,74"/>
      </g>
    </g>
    <g class="step step--monitoring" transform="translate(457,545)" filter="url(#soft-shadow)">
      <use href="#step-shape" fill="url(#grad-monitoring)"/>
      <polygon points="0,56 56,0 112,56 56,112" fill="url(#grad-monitoring)"/>
      <g fill="none" stroke="#fff" stroke-width="2.5">
        <rect x="25" y="36" width="48" height="34"/><line x1="42" y1="78" x2="56" y2="78"/><line x1="49" y1="70" x2="49" y2="78"/>
        <polyline points="30,54 38,54 42,46 46,60 50,52 54,54"/>
        <circle cx="64" cy="58" r="9" fill="var(--magenta)"/><line x1="70" y1="65" x2="80" y2="75" stroke-width="4"/>
      </g>
    </g>
    <g class="step step--testing" transform="translate(399,685)" filter="url(#soft-shadow)">
      <use href="#step-shape" fill="url(#grad-testing)"/>
      <polygon points="0,56 56,0 112,56 56,112" fill="url(#grad-testing)"/>
      <g fill="none" stroke="#fff" stroke-width="2">
        <rect x="30" y="28" width="40" height="54"/><rect x="44" y="24" width="12" height="6"/>
        <rect x="35" y="36" width="8" height="8"/><line x1="47" y1="40" x2="64" y2="40"/>
        <rect x="35" y="50" width="8" height="8"/><line x1="47" y1="54" x2="64" y2="54"/>
        <rect x="58" y="60" width="6" height="22"/><rect x="66" y="60" width="6" height="22"/><rect x="74" y="60" width="6" height="22"/><rect x="82" y="60" width="6" height="22"/>
      </g>
    </g>
    <g class="step step--barriers" transform="translate(336,819)" filter="url(#soft-shadow)">
      <use href="#step-shape" fill="url(#grad-barriers)"/>
      <polygon points="0,56 56,0 112,56 56,112" fill="url(#grad-barriers)"/>
      <g fill="#fff" stroke="#fff" stroke-width="1.5">
        <circle cx="32" cy="35" r="3"/><rect x="30" y="40" width="4" height="11"/>
        <circle cx="56" cy="35" r="3"/><rect x="54" y="40" width="4" height="11"/>
        <circle cx="80" cy="35" r="3"/><rect x="78" y="40" width="4" height="11"/>
        <circle cx="32" cy="63" r="3"/><rect x="30" y="68" width="4" height="11"/>
        <circle cx="56" cy="63" r="3"/><rect x="54" y="68" width="4" height="11"/>
        <circle cx="80" cy="63" r="3"/><rect x="78" y="68" width="4" height="11"/>
        <line x1="38" y1="44" x2="50" y2="44"/><line x1="62" y1="44" x2="74" y2="44"/>
        <line x1="38" y1="72" x2="50" y2="72"/><line x1="62" y1="72" x2="74" y2="72"/>
        <line x1="56" y1="53" x2="56" y2="60"/><line x1="32" y1="53" x2="32" y2="60"/>
      </g>
    </g>

    <!-- footer wave -->
    <path class="footer-wave" d="M0,1130 C250,1104 500,1126 700,1110 C800,1102 860,1092 900,1085 L900,1200 L0,1200 Z" fill="url(#grad-header)"/>
  </svg>

  <h1 class="header-title">CORONAVIRUS COVID-19</h1>
  <p class="header-subtitle">INFORMATION AND GUIDELINES</p>

  <div class="hub-label hub-label--the">THE</div>
  <div class="hub-label hub-label--exit">EXIT</div>
  <div class="hub-label hub-label--strategy">STRATEGY</div>

  <p class="step-text step-text--hospital"><strong>Ensure</strong>at all times, sufficient hospital capacities.</p>
  <p class="step-text step-text--resurgence">Foresee the possibility of reintroducing stricter measures in the event of a strong resurgence of the virus among the population</p>
  <p class="step-text step-text--monitoring">Provide close monitoring of the evolution of the pandemic during the entire exit, as well as the secondary effects of the confinement.</p>
  <p class="step-text step-text--testing">Foster testing capacities and support research in particular with regard to tests to measure the acquired immunity of the population.</p>
  <p class="step-text step-text--barriers">Apply basic barrier gestures and reinforce them with other specific measures, including in the workplace, to minimize the risk of an uncontrolled spread of the virus</p>

  <p class="closing"><b>PROTECT</b><br>IN PARTICULAR,<br><b>VULNERABLE</b> GROUPS.</p>
</main>
</body>
</html>
```